Real Estate Postcard for Record Sales - Let's Get the Word Out!

This is an QRPX direct mail piece. The size needs to be 6.5 x 9 horizontal. An insignia for QRPX direct mail needs to be included in design (I put what it needs to say on the mock up). The attached gives a basic idea of layout, but it needs the touch of a professional designer, no doubt! Please see "Tamsworth Front and Tamsworth Back" files for copy and general thoughts on positioning. I have set four multi county records with my clients sales and I've been much too quiet about it. It's time to get that word out!! Where it says "Call Now" - I see in a tasteful color bar. This is a piece that is going out to individuals that are upper middle to upper class. It needs to speak to that audience, while calling out these records. Personable, but not too playful. Bold, but in a classy way if that makes sense. My logo (Brightmoor Hearth) and colors take dominance over Pennick Thorne logo. The more we could work the color theme in with my logo, the better. My logo should also be larger than in the mockup. I believe I have attached all files. Any issues with the files LMK. The house filename will coordinate with the one noted on the back side of the piece. This will become my template for record sales. If you can fit my picture in without it looking crowded, that would be great. If not, I don't want to clutter to get it in. My picture is labeled (LoraVance.jpeg). Thanks so much!!!!

Target Market(s)

Upper middle to upper level home sellers, generally 45+ years of age.

Industry/Entity Type

Real Estate

Requirements
Must have
• Noted on mockups
Nice to have
• My picture
Should not have
• Colors that clash with my logo. My logo (Brightmoor Hearth) should set the tone for the piece.

```html
<!DOCTYPE html>
<html lang="en">
<head>
<meta charset="utf-8">
<title>Record Sale Postcard – Brightmoor Hearth</title>
<link rel="stylesheet" href="https://fonts.googleapis.com/css2?family=Oswald:wght@600;700&family=Libre+Caslon+Display&family=Montserrat:wght@700&display=swap">
<style>
  :root {
    --brown: #5c3b14;
    --brown-deep: #3d2607;
    --gold: #c9a62c;
    --white: #ffffff;
  }
  * { margin: 0; padding: 0; box-sizing: border-box; }
  html, body { width: 1200px; height: 867px; overflow: hidden; background: var(--white); }
  .postcard { position: relative; width: 1200px; height: 867px; overflow: hidden; background: var(--white); }
  .postcard__shapes { position: absolute; inset: 0; }
  .headline {
    position: absolute; left: 0; top: 100px; width: 612px;
    font-family: "Oswald", sans-serif; font-weight: 700;
    font-size: 64px; line-height: 66px; color: var(--brown);
    text-align: center; letter-spacing: 0.5px;
  }
  .record-label {
    position: absolute; left: 0; top: 372px; width: 582px;
    font-family: "Oswald", sans-serif; font-weight: 700;
    font-size: 76px; line-height: 90px; color: var(--brown);
    text-align: center;
  }
  .property { position: absolute; left: 0; width: 600px; text-align: center; font-family: "Libre Caslon Display", serif; }
  .property__name { top: 508px; font-size: 76px; line-height: 90px; color: var(--white); }
  .property__address { top: 614px; font-size: 27px; line-height: 34px; color: var(--gold); }
  .property__note { top: 674px; font-size: 27px; line-height: 34px; color: var(--white); }
  .brand {
    position: absolute; left: 652px; top: 452px; width: 500px; height: 76px;
    display: flex; align-items: center; gap: 22px;
  }
  .brand__mark { flex: 0 0 68px; height: 68px; border-radius: 50%; background: var(--gold); }
  .brand__name {
    font-family: "Libre Caslon Display", serif; font-size: 44px; line-height: 60px;
    color: var(--brown); white-space: nowrap;
  }
  .cta-pill {
    position: absolute; left: 876px; top: 694px; width: 185px; height: 47px;
    border-radius: 24px; background: var(--gold);
    font-family: "Montserrat", sans-serif; font-weight: 700; font-size: 23px;
    line-height: 47px; text-align: center; color: var(--white); letter-spacing: 0.5px;
  }
  .cta-phone {
    position: absolute; left: 778px; top: 746px; width: 380px; text-align: center;
    font-family: "Oswald", sans-serif; font-weight: 600; font-size: 62px;
    line-height: 76px; color: var(--white);
  }
</style>
</head>
<body>
<main class="postcard">
  <svg class="postcard__shapes" width="1200" height="867" viewBox="0 0 1200 867">
    <defs>
      <linearGradient id="brown-fill" x1="0" y1="0" x2="0" y2="1">
        <stop offset="0" stop-color="#5a3a14"/>
        <stop offset="1" stop-color="#3d2607"/>
      </linearGradient>
      <linearGradient id="band-fill" x1="0" y1="0" x2="1" y2="0">
        <stop offset="0" stop-color="#3d2607"/>
        <stop offset="1" stop-color="#5e3f16"/>
      </linearGradient>
      <linearGradient id="photo-fill" x1="0" y1="0" x2="1" y2="1">
        <stop offset="0" stop-color="#eeebe4"/>
        <stop offset="0.55" stop-color="#c9bfae"/>
        <stop offset="1" stop-color="#6e4427"/>
      </linearGradient>
    </defs>
    <path class="gold-band" d="M0 367 L440 367 C520 367 560 400 590 450 L815 867 L0 867 Z" fill="var(--gold)"/>
    <path class="brown-panel" d="M0 459 L500 459 C540 459 562 480 580 512 L780 867 L0 867 Z" fill="url(#brown-fill)"/>
    <path class="cta-band" d="M744 717 L1200 717 L1200 867 L826 867 Z" fill="url(#band-fill)"/>
    <path class="feature-photo" role="img" aria-label="Photo of the sold home's bright open kitchen and dining room with chandelier and hardwood floors" d="M478 0 L1200 0 L1200 408 L790 408 C730 408 705 392 682 352 Z" fill="url(#photo-fill)"/>
    <path class="photo-rule" d="M452 0 L665 356 C697 412 735 428 795 428 L1200 432" fill="none" stroke="var(--gold)" stroke-width="3.5"/>
  </svg>

  <h1 class="headline">Get Noticed<br>with the attention<br>your home deserves!</h1>

  <h2 class="record-label">RECORD SALE!</h2>

  <p class="property property__name">The Tamsworth</p>
  <p class="property property__address">27 Ashcombe Lane</p>
  <p class="property property__note">Highest transaction dollar sale in<br>the history of the Upper Ridge MLS for<br>attached residence in The Tamsworth<br>- and this wasn't even an end unit!</p>

  <div class="brand">
    <span class="brand__mark"></span>
    <p class="brand__name">Brightmoor Hearth</p>
  </div>

  <p class="cta-pill">CALL NOW</p>
  <p class="cta-phone">555-284-1937</p>
</main>
</body>
</html>
```